Poetry Book Cover Design Project

Looking for a minimalistic book cover design for a collection of poems. The book title is "Before The Morning Turns To Glass". There are three parts to the book. First covers poetry in the theme of Rage. Second love and desire. The third is strange poems. Essentially the sections are "Rage", "Desire" and the "Strange". The reason for the title "Before The Morning Turns To Glass" is as if someone is writing these till life changes towards the intended outcome as felt in each poem. I want to have the author's name "Nirosha Kulathunge" at the bottom. Ilustration attached.
- Minimalistic

```html
<!DOCTYPE html>
<html lang="en">
<head>
<meta charset="utf-8">
<title>Before The Morning Turns To Glass — Nirosha Kulathunge</title>
<link rel="stylesheet" href="https://fonts.googleapis.com/css2?family=Abril+Fatface&family=Montserrat:wght@400;700&display=swap">
<style>
  :root {
    --backdrop: #e9ecec;
    --cover: #fbfbfb;
    --ink: #151515;
    --wash-plum: #7a2f63;
    --wash-violet: #5a4a8c;
    --wash-indigo: #274f86;
    --wash-blue: #1f6fa3;
    --wash-teal: #149a99;
    --wash-green: #2fb06a;
    --wash-aqua: #1fa6a0;
  }
  * { margin: 0; padding: 0; box-sizing: border-box; }
  html, body {
    width: 1200px;
    height: 1200px;
    overflow: hidden;
    background: var(--backdrop);
  }
  .stage {
    width: 1200px;
    height: 1200px;
    display: flex;
    align-items: center;
    justify-content: center;
  }
  .book-cover {
    position: relative;
    width: 790px;
    height: 1140px;
    background: var(--cover);
  }
  .title {
    position: absolute;
    top: 30px;
    right: 88px;
    font-family: "Abril Fatface", "Playfair Display", serif;
    font-weight: 400;
    font-size: 158px;
    line-height: 143px;
    letter-spacing: -2px;
    text-align: right;
    color: transparent;
    background:
      radial-gradient(ellipse 60% 18% at 40% 4%, var(--wash-plum) 0%, transparent 70%),
      radial-gradient(ellipse 40% 20% at 20% 38%, var(--wash-plum) 0%, transparent 75%),
      radial-gradient(ellipse 50% 20% at 85% 55%, var(--wash-green) 0%, transparent 75%),
      radial-gradient(ellipse 45% 18% at 30% 68%, var(--wash-indigo) 0%, transparent 75%),
      linear-gradient(180deg, var(--wash-violet) 0%, var(--wash-indigo) 22%, var(--wash-blue) 45%, var(--wash-teal) 65%, var(--wash-aqua) 85%, var(--wash-teal) 100%);
    -webkit-background-clip: text;
    background-clip: text;
  }
  .title-line {
    display: flex;
    justify-content: flex-end;
    align-items: center;
  }
  .series-label {
    font-family: "Montserrat", sans-serif;
    font-size: 23px;
    line-height: 29px;
    letter-spacing: 0.5px;
    font-weight: 400;
    color: var(--ink);
    -webkit-text-fill-color: var(--ink);
    text-align: right;
    margin-right: 14px;
    margin-top: 8px;
  }
  .series-label strong { font-weight: 700; }
  .author {
    position: absolute;
    right: 90px;
    top: 1000px;
    font-family: "Montserrat", sans-serif;
    font-weight: 700;
    font-size: 27px;
    line-height: 44px;
    letter-spacing: 2.5px;
    text-align: right;
    color: var(--ink);
    text-transform: uppercase;
  }
</style>
</head>
<body>
  <main class="stage">
    <section class="book-cover">
      <h1 class="title">
        <span class="title-line">before</span>
        <span class="title-line">the</span>
        <span class="title-line">morning</span>
        <span class="title-line"><span class="series-label">COLLECTION<br>OF <strong>POEMS</strong></span>turns</span>
        <span class="title-line">to</span>
        <span class="title-line">glass.</span>
      </h1>
      <p class="author">Nirosha<br>Kulathunge</p>
    </section>
  </main>
</body>
</html>
```